Ravel Oversight Partners - Statonery Design

I just completed a redesign of my business card. Please do not design a logo or business card. See my current stationery design attached.

Target Market(s)

VP of Human Resources and Finance - Companies with 100 employees to 10,000

Industry/Entity Type

Business Consultant

Requirements
Must have
• Use the letterhead instructions for the color and fonts.

```html
<!DOCTYPE html>
<html lang="en">
<head>
<meta charset="utf-8">
<title>Ravel Oversight Partners – Stationery</title>
<link rel="stylesheet" href="https://fonts.googleapis.com/css2?family=Libre+Baskerville&family=Montserrat:ital,wght@0,400;0,500;1,600&display=swap">
<style>
  :root {
    --plum: #6b2b4e;
    --slate: #68676c;
    --paper: #e9e9ea;
    --ink: #222;
    --muted: #555;
    --backdrop: #2b2b2d;
  }
  * { margin: 0; padding: 0; box-sizing: border-box; }
  html, body { width: 1200px; height: 1081px; overflow: hidden; background: var(--backdrop); }
  body { position: relative; font-family: "Montserrat", sans-serif; color: var(--ink); }

  .sheet { position: absolute; background: var(--paper); overflow: hidden; box-shadow: 0 2px 8px rgba(0,0,0,.45); }
  .letterhead { left: 31px; top: 190px; width: 504px; height: 712px; }
  .envelope-front { left: 602px; top: 252px; width: 564px; height: 269px; }
  .envelope-back { left: 604px; top: 597px; width: 565px; height: 269px; }

  .brand { position: absolute; display: flex; align-items: center; gap: 9px; }
  .brand-dot { width: 56px; height: 56px; border-radius: 50%; background: var(--plum); flex: none; }
  .brand-name { font-family: "Libre Baskerville", serif; font-size: 17px; line-height: 22px; color: var(--slate); }

  .contact { position: absolute; border-left: 1px solid #999; padding-left: 8px; font-size: 7.5px; line-height: 12px; color: var(--muted); }
  .contact .row { display: flex; align-items: center; gap: 6px; }
  .contact svg { width: 7px; height: 7px; flex: none; }
  .contact .address { margin-top: 4px; }

  .letterhead .brand { left: 49px; top: 36px; }
  .letterhead .contact { left: 313px; top: 36px; }
  .letter { position: absolute; left: 48px; top: 180px; width: 409px; font-size: 9.2px; line-height: 14.4px; }
  .letter .date { margin-bottom: 15px; }
  .letter .recipient { margin-bottom: 26px; }
  .letter .salutation { font-style: italic; font-weight: 600; font-size: 10px; margin-left: 2px; margin-bottom: 20px; }
  .letter p.body { text-align: justify; margin-bottom: 14.4px; }
  .signature { position: absolute; left: 333px; top: 593px; width: 78px; height: 22px; background: linear-gradient(90deg, #cfcfd0, #9a9a9c, #cfcfd0); border-radius: 8px; }
  .signer { position: absolute; left: 333px; top: 625px; font-size: 9px; line-height: 10px; }
  .signer small { display: block; font-size: 7.5px; }

  .band { position: absolute; left: 0; bottom: 0; width: 100%; }

  .envelope-front .brand { left: 22px; top: 23px; }
  .envelope-front .contact { left: 80px; top: 196px; }

  .flap { position: absolute; left: 0; top: 0; width: 100%; height: 96px; }
  .flap-dot { position: absolute; left: 254px; top: 20px; width: 56px; height: 56px; border-radius: 50%; background: var(--plum); }
</style>
</head>
<body>

<svg width="0" height="0" style="position:absolute">
  <symbol id="icon-phone" viewBox="0 0 10 10"><path d="M6 1.5C4 1.5 2.5 4 2.5 6.5 2.5 8 3 9 3 9L4.3 8.2C4 7.3 4 5 5.5 3.2Z" fill="var(--plum)"/></symbol>
  <symbol id="icon-mail" viewBox="0 0 10 10"><rect x="0.5" y="2" width="9" height="6" fill="var(--plum)"/><path d="M0.5 2 5 5.5 9.5 2" stroke="#fff" stroke-width="1" fill="none"/></symbol>
</svg>

<section class="sheet letterhead">
  <div class="brand">
    <span class="brand-dot"></span>
    <span class="brand-name">Ravel Oversight<br>Partners</span>
  </div>
  <address class="contact" style="font-style:normal">
    <div class="row"><svg><use href="#icon-phone"/></svg>555.210.4471</div>
    <div class="row"><svg><use href="#icon-mail"/></svg>raveloversight.com</div>
    <div class="address">118 Alder Street, Suite 300<br>Lakeview, MN 55012</div>
  </address>

  <article class="letter">
    <p class="date">January 14, 2016</p>
    <p class="recipient">Mr. Sam Ellery<br>Photographer</p>
    <p class="salutation">Dear Mr. Sam Ellery</p>
    <p class="body">Lorem ipsum dolor sit amet, consectetur adipiscing elit. Ut feugiat erat interdum augue interdum, vitae fringilla ante vehicula. Pellentesque ultrices nulla id accumsan scelerisque. Suspendisse vitae luctus dui. Cras sed dictum lorem. Donec non gravida lacus. Phasellus et quam et mi commodo malesuada ac bibendum lorem. Fusce eleifend, metus vel convallis fringilla, ipsum dui egestas arcu, at hendrerit elit nisl eget metus. Proin eget fringilla eros. Nunc eros metus, molestie in ligula non, imperdiet lobortis massa. Proin accumsan posuere erat, vitae adipiscing sem commodo eu.</p>
    <p class="body">Morbi a faucibus nulla. Nulla id leo ac massa fermentum molestie. Integer at gravida risus. Sed auctor odio augue. Mauris eu leo a orci placerat bibendum sed ac nulla. Sed risus mauris, vestibulum sit amet egestas at, pulvinar sed mauris. In velit purus, laoreet ac lectus vitae, ornare posuere tortor. Phasellus mattis accumsan vestibulum.</p>
    <p class="body">Donec cursus libero id convallis egestas. Aliquam quam quam, facilisis eget diam at, ultricies sagittis justo. Integer massa nibh, gravida eu nulla sagittis, feugiat ultrices magna. Ut commodo venenatis tortor, sed dignissim mauris congue non.</p>
  </article>

  <div class="signature" role="img" aria-label="Handwritten signature"></div>
  <p class="signer">Lee Marsh,<small>Photographer</small></p>

  <svg class="band" height="13" viewBox="0 0 504 13" preserveAspectRatio="none">
    <rect width="504" height="13" fill="var(--slate)"/>
    <polygon points="0,0 348,0 341,13 0,13" fill="var(--plum)"/>
    <polygon points="348,0 352,0 345,13 341,13" fill="#fff"/>
  </svg>
</section>

<section class="sheet envelope-front">
  <div class="brand">
    <span class="brand-dot"></span>
    <span class="brand-name">Ravel Oversight<br>Partners</span>
  </div>
  <address class="contact" style="font-style:normal">
    <div class="row"><svg><use href="#icon-phone"/></svg>555.210.4471</div>
    <div class="row"><svg><use href="#icon-mail"/></svg>raveloversight.com</div>
    <div class="address">118 Alder Street, Suite 300<br>Lakeview, MN 55012</div>
  </address>
  <svg class="band" height="12" viewBox="0 0 564 12" preserveAspectRatio="none">
    <rect width="564" height="12" fill="var(--slate)"/>
    <polygon points="0,0 400,0 394,12 0,12" fill="var(--plum)"/>
    <polygon points="400,0 404,0 398,12 394,12" fill="#fff"/>
  </svg>
</section>

<section class="sheet envelope-back">
  <svg class="flap" viewBox="0 0 565 96" preserveAspectRatio="none">
    <path d="M0 0H565L552 84Q550 94 538 94H26Q14 94 12 84Z" fill="var(--slate)"/>
  </svg>
  <span class="flap-dot"></span>
</section>

</body>
</html>
```